" Loja agropecuária ,vendemos rações medicamentos,acessórios veterinários e agrícolas e estamos vendo a possibilidade de implantar o serviço de banho e tosa na loja. "

```html
<!DOCTYPE html>
<html lang="pt-BR">
<head>
<meta charset="UTF-8">
<title>Cartão de visitas – Agropecuária Vale Verde</title>
<link rel="stylesheet" href="https://fonts.googleapis.com/css2?family=Open+Sans:wght@400;700;800&display=swap">
<style>
  :root {
    --page: #ececec;
    --card-white: #ffffff;
    --card-white-shade: #f0f0f0;
    --green-dark: #0f4d23;
    --green: #1a6b32;
    --green-light: #2a8a43;
    --gold: #d8b331;
    --gold-light: #f3d868;
    --text-light: #ffffff;
  }
  * { box-sizing: border-box; margin: 0; padding: 0; }
  html, body {
    width: 1200px; height: 1200px; overflow: hidden;
    background: var(--page);
    font-family: "Open Sans", Arial, sans-serif;
  }
  .card-set {
    position: absolute; left: 195px; top: 138px; width: 810px;
    box-shadow: 0 10px 30px rgba(0,0,0,.25);
  }
  .card { position: relative; width: 810px; overflow: hidden; }

  /* Front */
  .card--front {
    height: 444px;
    background: linear-gradient(180deg, var(--card-white) 0%, var(--card-white) 70%, var(--card-white-shade) 100%);
  }
  .brand {
    position: absolute; display: flex; align-items: center; gap: 14px;
    font-weight: 800; color: var(--green); line-height: 1;
  }
  .brand__mark { border-radius: 50%; background: var(--gold); flex: none; }
  .brand__name { display: flex; flex-direction: column; align-items: center; }
  .brand__kicker { letter-spacing: .32em; }
  .card--front .brand { left: 50%; top: 50%; transform: translate(-50%, -40%); }
  .card--front .brand__mark { width: 44px; height: 44px; }
  .card--front .brand__kicker { font-size: 18px; margin-bottom: 8px; }
  .card--front .brand__title { font-size: 58px; letter-spacing: .01em; }

  /* Back */
  .card--back {
    height: 480px;
    background: radial-gradient(ellipse at 45% 40%, var(--green-light) 0%, var(--green) 45%, var(--green-dark) 100%);
    color: var(--text-light);
  }
  .card--back .brand { left: 60px; top: 150px; color: var(--text-light); }
  .card--back .brand__mark { width: 34px; height: 34px; }
  .card--back .brand__kicker { font-size: 14px; margin-bottom: 6px; }
  .card--back .brand__title { font-size: 42px; }

  .contact { position: absolute; left: 427px; top: 132px; width: 300px; }
  .contact__name { font-size: 34px; font-weight: 700; line-height: 1.1; }
  .contact__role { font-size: 24px; text-align: right; margin-top: 4px; }
  .contact__phone {
    display: flex; align-items: center; gap: 10px;
    font-size: 34px; margin: 32px 0 0 20px;
  }
  .contact__line {
    display: flex; align-items: center; gap: 10px;
    font-size: 23px; margin-left: 2px; margin-top: 10px;
  }
  .contact__line:first-of-type { margin-top: 26px; }
  .social { position: absolute; left: 655px; top: 412px; display: flex; gap: 8px; }
  .social__item { width: 24px; height: 24px; background: var(--text-light); border-radius: 3px; }

  .gold-rule {
    position: absolute; left: 0; right: 0; top: 455px; height: 5px;
    background: linear-gradient(90deg, var(--gold), var(--gold-light) 50%, var(--gold));
  }
  .bottom-band {
    position: absolute; left: 0; right: 0; top: 460px; bottom: 0;
    background: var(--green-dark);
  }
</style>
</head>
<body>
  <div class="card-set">
    <section class="card card--front">
      <div class="brand">
        <span class="brand__mark"></span>
        <span class="brand__name">
          <span class="brand__kicker">AGROPECUÁRIA</span>
          <span class="brand__title">VALE VERDE</span>
        </span>
      </div>
    </section>

    <section class="card card--back">
      <div class="brand">
        <span class="brand__mark"></span>
        <span class="brand__name">
          <span class="brand__kicker">AGROPECUÁRIA</span>
          <span class="brand__title">VALE VERDE</span>
        </span>
      </div>

      <div class="contact">
        <p class="contact__name">Nome Completo</p>
        <p class="contact__role">Função</p>
        <p class="contact__phone">
          <svg width="30" height="30" viewBox="0 0 24 24" aria-hidden="true">
            <circle cx="12" cy="12" r="10.5" fill="none" stroke="#fff" stroke-width="1.6"/>
            <path d="M9 6.5c-1 .5-1.8 1.6-1.5 3 .6 3 3.6 6.3 6.5 7.4 1.3.5 2.5-.2 3-1.1l-2-1.8-1.3.8c-1.3-.6-2.7-2.1-3.2-3.4l.9-1.2z" fill="#fff"/>
          </svg>
          00 0000-0000
        </p>
        <p class="contact__line">
          <svg width="20" height="16" viewBox="0 0 20 16" aria-hidden="true">
            <rect x="1" y="1" width="18" height="14" fill="none" stroke="#fff" stroke-width="1.5"/>
            <path d="M1 1l9 8 9-8" fill="none" stroke="#fff" stroke-width="1.5"/>
          </svg>
          contato@valeverde.com.br
        </p>
        <p class="contact__line">
          <svg width="20" height="20" viewBox="0 0 20 20" aria-hidden="true">
            <path d="M6 2v11l3-2.5 2 5 2-1-2-4.8h4z" fill="none" stroke="#fff" stroke-width="1.5" stroke-linejoin="round"/>
          </svg>
          www.valeverde.com.br
        </p>
      </div>

      <div class="social">
        <span class="social__item"></span>
        <span class="social__item"></span>
      </div>

      <div class="gold-rule"></div>
      <div class="bottom-band"></div>
    </section>
  </div>
</body>
</html>
```